Outdoor sign for Brindle Auto Restoration

I need a horizontal 4'x 8' outdoor roadside sign for my classic auto restoration business. I have uploaded colors and our logo. Needs the Brindle name, a prominent Classic AUTO RESTORATION, phone number and website. We rebuild and restore vintage cars, trucks and 4x4s. I'd like something clean but possibly retro. Classic Auto Restoration is more important than the Brindle name. It needs to be visible and readable from the street. NO CLIP ART

Target Market(s)

Customers who need their vintage care restored or upgraded. Men and women ages 25-75

Industry/Entity Type

Automotive

Colors
FFC000
F8CF3A
FAE287
FDF2CF
FEFAEE

Requirements
Must have
• Legible. Bright. Readable as a backlit 4' x 8' large horizontal sign (roughly 120cm X 240cm)
Nice to have
• Use of the Brindle logo/type, Complete or Classic before prominent AUTO RESTORATION
Should not have
• Clip art of old cars or icons. And we don't want the Brindle Logo from the website because it wont be legible from the road. I have included the Illustrator file for Brindle text in the uploads

```html
<!DOCTYPE html>
<html lang="en">
<head>
<meta charset="utf-8">
<title>Brindle Auto Restoration – Roadside Sign</title>
<link rel="stylesheet" href="https://fonts.googleapis.com/css2?family=Roboto+Condensed:wght@700&display=swap">
<style>
  :root {
    --page-bg: #ececec;
    --amber: #f6a531;
    --gold: #ffc000;
    --sun: #f8cf3a;
    --butter: #fae287;
    --cream: #fdf2cf;
    --ink: #0a0b0c;
    --paper: #ffffff;
  }
  * { margin: 0; padding: 0; box-sizing: border-box; }
  html, body {
    width: 1200px;
    height: 1200px;
    overflow: hidden;
    background: var(--page-bg);
  }
  .canvas {
    position: relative;
    width: 1200px;
    height: 1200px;
  }
  .roadside-sign {
    position: absolute;
    left: 50px;
    top: 326px;
    width: 1100px;
    height: 548px;
    display: block;
  }
  .wordmark text {
    font-family: "Roboto Condensed", "Arial Narrow", sans-serif;
    font-weight: 700;
    fill: var(--ink);
  }
  .wordmark-name { font-size: 116px; }
  .wordmark-classic { font-size: 112px; }
  .wordmark-service { font-size: 46px; letter-spacing: 2px; }
  .sign-contact {
    font-family: "Roboto Condensed", "Arial Narrow", sans-serif;
    font-weight: 700;
    font-size: 52px;
    fill: var(--paper);
  }
  .contact-divider { fill: var(--gold); }
  .footer-band { fill: var(--ink); }
</style>
</head>
<body>
<main class="canvas">
  <svg class="roadside-sign" viewBox="0 0 1100 548" xmlns="http://www.w3.org/2000/svg" aria-label="Brindle Classic Auto Restoration sign">
    <defs>
      <radialGradient id="glow" cx="0.5" cy="0.55" r="0.7">
        <stop offset="0" stop-color="var(--cream)"/>
        <stop offset="0.45" stop-color="var(--butter)"/>
        <stop offset="0.85" stop-color="var(--sun)"/>
        <stop offset="1" stop-color="var(--amber)"/>
      </radialGradient>
      <linearGradient id="topWash" x1="0" y1="0" x2="0" y2="1">
        <stop offset="0" stop-color="var(--gold)" stop-opacity="0.75"/>
        <stop offset="0.3" stop-color="var(--sun)" stop-opacity="0.25"/>
        <stop offset="0.55" stop-color="var(--butter)" stop-opacity="0"/>
      </linearGradient>
    </defs>

    <rect class="sign-field" width="1100" height="548" fill="url(#glow)"/>
    <rect class="sign-field-wash" width="1100" height="548" fill="url(#topWash)"/>

    <g class="wordmark" text-anchor="middle">
      <text class="wordmark-name" x="580" y="142">BRINDLE</text>
      <text class="wordmark-classic" x="580" y="256">CLASSIC</text>
      <text class="wordmark-service" x="580" y="314">AUTO RESTORATION</text>
    </g>

    <path class="footer-band" d="M0 461 Q540 250 1100 466 L1100 548 L0 548 Z"/>

    <text class="sign-contact" x="126" y="486">501-555-0142</text>
    <circle class="contact-divider" cx="441" cy="472" r="9"/>
    <text class="sign-contact" x="490" y="486">brindle autoworks.com</text>
  </svg>
</main>
</body>
</html>
```